"Thank You" flyer design

We need a "thank you" flyer that will be sent out with all our products.
a6 size landscape,
We manufacture personalised shaped signs.
I've attached a rough idea of what we are after, but would like it to be improved upon with some artistic flare..

Side one - We would like the flyer to have a simple message - "thank you for shopping with us"

Side two - we would also like our logo and a union jack made in the UK badge and our address and contact details with our website www.lumkinprints.co.uk being the most prominent..

We are after a simple bold design what would be printed on a small a6 card that people might hopefully want to keep, so the end design needs to be pretty cool.

Industry/Entity Type

Shopping

Font styles to use
Serif
Sans Serif

```html
<!DOCTYPE html>
<html lang="en">
<head>
<meta charset="utf-8">
<title>Lumkin Prints – Thank You Flyer</title>
<link rel="stylesheet" href="https://fonts.googleapis.com/css2?family=Allura&family=Fredoka:wght@600&family=Open+Sans:wght@300;400;600&display=swap">
<style>
  :root {
    --brand-pink: #e5318f;
    --card-white: #ffffff;
    --card-edge: #d9d9d9;
    --ink-grey: #4a4a4a;
    --badge-blue: #2b3f7e;
    --badge-red: #c8202f;
  }
  * { box-sizing: border-box; margin: 0; padding: 0; }
  html, body {
    width: 1200px; height: 500px; overflow: hidden;
    background: var(--card-white);
    font-family: "Open Sans", Arial, sans-serif;
    color: var(--ink-grey);
  }
  .canvas { position: relative; width: 1200px; height: 500px; }
  .card {
    position: absolute; top: 59px; width: 532px; height: 379px;
    border: 1px solid var(--card-edge); background: var(--card-white);
  }
  .card--front { left: 49px; }
  .card--back { left: 602px; }

  .thank-you-panel { position: absolute; left: 107px; top: 71px; width: 318px; height: 236px; }
  .thank-you-panel svg { position: absolute; inset: 0; }
  .message {
    position: absolute; inset: 0;
    display: flex; flex-direction: column; align-items: center;
    color: var(--card-white); text-align: center;
  }
  .message__thank {
    margin-top: 34px;
    font-family: "Fredoka", "Arial Rounded MT Bold", sans-serif;
    font-weight: 600; font-size: 64px; line-height: 64px; letter-spacing: 1px;
  }
  .message__you {
    margin-top: -4px;
    font-family: "Fredoka", "Arial Rounded MT Bold", sans-serif;
    font-weight: 600; font-size: 96px; line-height: 88px; letter-spacing: 2px;
  }
  .message__tagline {
    margin-top: 0;
    font-family: "Allura", cursive;
    font-size: 40px; line-height: 42px;
  }

  .brand-mark { position: absolute; left: 22px; top: 92px; width: 84px; height: 84px; background: var(--brand-pink); }
  .brand-name {
    position: absolute; left: 14px; top: 186px; width: 120px;
    font-weight: 600; font-size: 15px; line-height: 18px; color: var(--brand-pink);
  }
  .address {
    position: absolute; left: 159px; top: 80px;
    font-size: 8.5px; line-height: 12px; font-style: normal; color: var(--ink-grey);
  }
  .web-band { position: absolute; left: 112px; top: 146px; width: 419px; height: 44px; }
  .web-band svg { position: absolute; inset: 0; }
  .web-address {
    position: absolute; left: 48px; top: 3px;
    font-weight: 300; font-size: 30px; line-height: 38px; color: var(--card-white);
    letter-spacing: -0.2px; white-space: nowrap;
  }
  .contact { position: absolute; left: 159px; top: 195px; font-size: 13px; line-height: 21px; color: var(--ink-grey); }
  .uk-badge { position: absolute; left: 157px; top: 248px; width: 118px; height: 68px; }
</style>
</head>
<body>
<main class="canvas">
  <section class="card card--front" aria-label="Front of flyer">
    <div class="thank-you-panel">
      <svg viewBox="0 0 318 236" preserveAspectRatio="none" aria-hidden="true">
        <path d="M3 2 L90 4 L180 1 L262 3 L316 2 L315 60 L317 130 L314 200 L316 234 L230 232 L140 235 L60 233 L2 234 L4 170 L1 100 L3 40 Z" fill="var(--brand-pink)"/>
      </svg>
      <h1 class="message">
        <span class="message__thank">THANK</span>
        <span class="message__you">YOU</span>
        <span class="message__tagline">for shopping with us</span>
      </h1>
    </div>
  </section>

  <section class="card card--back" aria-label="Back of flyer">
    <div class="brand-mark"></div>
    <div class="brand-name">Lumkin Prints</div>

    <address class="address">
      Lumkin Prints Ltd<br>
      Unit 8 Harlow Street<br>
      Brindlecombe<br>
      Westshire<br>
      WS4 2LP
    </address>

    <div class="web-band">
      <svg viewBox="0 0 419 44" preserveAspectRatio="none" aria-hidden="true">
        <path d="M0 3 L80 1 L170 3 L260 0 L350 2 L419 1 L417 12 L419 24 L417 36 L419 43 L330 41 L240 44 L150 42 L60 43 L0 41 Z" fill="var(--brand-pink)"/>
      </svg>
      <span class="web-address">www.lumkinprints.co.uk</span>
    </div>

    <div class="contact">
      <div class="phone">01632 960418</div>
      <div class="email">sales@lumkinprints.co.uk</div>
    </div>

    <svg class="uk-badge" viewBox="0 0 118 68" role="img" aria-label="Made in the UK badge">
      <rect x="0" y="0" width="118" height="68" rx="3" fill="var(--badge-blue)"/>
      <rect x="0" y="26" width="118" height="16" fill="var(--badge-red)"/>
    </svg>
  </section>
</main>
</body>
</html>
```